RM Straßenlogistik Kundenflyer
Zielgruppe
Wir sind ein Verkehrssicherheitsdienstleister aus der Region Heilbronn und Umgebung. Zu unseren Kunden zählen z.B. Bauunternehmen, Dachdecker, Kellerbauer, Kranfirmen, Hausbauer, Holzbauer und Privatpersonen.
Leistungen:
Erstellen von Verkehrszeichenplänen
Einholen von Genehmigungen
Stellen von Straßensperrungen und Parkverboten
Vermietung von Verkehrszeichen
Aufgabenstellung
Aussagekräftige Bilder, nicht zu viel Text. Die Farbe der Verkehrssicherung ist Rot. Daher sollte der Flyer Weiß / Rot sein. kurze Beschreibung unserer Leistungen.

```html
<!DOCTYPE html>
<html lang="de">
<head>
<meta charset="utf-8">
<title>RM Straßenlogistik – Kundenflyer</title>
<link rel="stylesheet" href="https://fonts.googleapis.com/css2?family=DM+Sans:wght@500;700&family=Inter:wght@400&display=swap">
<style>
  :root {
    --red: #e93a36;
    --red-soft: #f0625e;
    --white: #ffffff;
    --ink: #1b1b1b;
    --page-bg: #f4f4f4;
    --amber: #f39a2a;
    --sky: #7fa6d6;
  }
  * { margin: 0; padding: 0; box-sizing: border-box; }
  html, body { width: 1200px; height: 1200px; overflow: hidden; background: var(--page-bg); }
  .flyer {
    position: absolute; left: 204px; top: 40px;
    width: 791px; height: 1120px;
    background: var(--white);
    overflow: hidden;
  }
  .top-bar { position: absolute; left: 0; top: 0; width: 100%; height: 12px; background: var(--red); }
  .brand {
    position: absolute; left: 65px; top: 84px;
    display: flex; align-items: center; gap: 10px;
    font-family: "DM Sans", sans-serif; font-weight: 700;
    font-size: 25px; color: var(--red);
  }
  .brand-square { width: 28px; height: 28px; background: var(--red); border-radius: 4px; }
  .contact {
    position: absolute; right: 69px; top: 57px;
    text-align: right; font-style: normal;
    font-family: "Inter", sans-serif; font-size: 14px; line-height: 17px; color: var(--ink);
  }
  .contact p + p { margin-top: 10px; }
  .headline {
    position: absolute; left: 66px; top: 198px;
    font-family: "DM Sans", sans-serif; font-weight: 500;
    font-size: 51px; line-height: 61px; color: var(--red);
    letter-spacing: 0.2px; white-space: nowrap;
  }
  .intro {
    position: absolute; left: 67px; top: 352px; width: 680px;
    font-family: "Inter", sans-serif; font-size: 13.8px; line-height: 17.5px; color: var(--ink);
  }
  .services { position: absolute; left: 67px; top: 424px; list-style: none; }
  .services li {
    display: flex; align-items: center; height: 19px;
    font-family: "DM Sans", sans-serif; font-weight: 500;
    font-size: 19px; color: var(--red); white-space: nowrap;
  }
  .services li + li { margin-top: 10px; }
  .services li:nth-child(n+3) { margin-top: 12px; }
  .services svg { width: 17px; height: 17px; margin-right: 30px; flex: none; }
  .gallery {
    position: absolute; left: 68px; top: 584px;
    display: grid; grid-template-columns: 320px 320px; gap: 13px 15px;
  }
  .photo-frame { width: 320px; height: 225px; background: var(--red); padding: 15px 17px; }
  .photo { width: 100%; height: 100%; }
  .photo-lamps { background: linear-gradient(135deg, var(--amber), var(--red-soft)); }
  .photo-road { background: linear-gradient(135deg, #e9b060, #7a8a9a); }
  .photo-sign { background: linear-gradient(135deg, var(--sky), #d8dde3); }
  .photo-beacons { background: linear-gradient(135deg, var(--red-soft), var(--amber)); }
  .footer-band {
    position: absolute; left: 0; bottom: 0; width: 100%; height: 36px;
    background: var(--red);
  }
</style>
</head>
<body>
  <main class="flyer">
    <div class="top-bar"></div>

    <div class="brand"><span class="brand-square"></span>RM Straßenlogistik</div>

    <address class="contact">
      <p>Am Lindenhang 7,<br>74199 Wiesental</p>
      <p>07100 5550123</p>
      <p>kontakt@rm-strassenlogistik.de</p>
    </address>

    <h1 class="headline">Ihre Sicherheit Ist<br>unser Anliegen</h1>

    <p class="intro">RM Straßenlogistik: Ihr Partner für Verkehrssicherheit. Wir bieten maßgeschneiderte Konzepte<br>und umfassende Dienstleistungen mit Fokus auf Qualität, Flexibilität und Sicherheit.</p>

    <ul class="services">
      <li><svg viewBox="0 0 17 17"><rect width="17" height="17" fill="#e93a36"/><path d="M4 9 L7.5 13 L13 3" stroke="#fff" stroke-width="1.8" fill="none"/></svg>Planung und Genehmigungsmanagement</li>
      <li><svg viewBox="0 0 17 17"><rect width="17" height="17" fill="#e93a36"/><path d="M4 9 L7.5 13 L13 3" stroke="#fff" stroke-width="1.8" fill="none"/></svg>Halteverbot</li>
      <li><svg viewBox="0 0 17 17"><rect width="17" height="17" fill="#e93a36"/><path d="M4 9 L7.5 13 L13 3" stroke="#fff" stroke-width="1.8" fill="none"/></svg>Vollsperrungen und halbseitige Sperrungen</li>
      <li><svg viewBox="0 0 17 17"><rect width="17" height="17" fill="#e93a36"/><path d="M4 9 L7.5 13 L13 3" stroke="#fff" stroke-width="1.8" fill="none"/></svg>Verleih von Verkehrsschildern und Baustellenabsicherung</li>
    </ul>

    <section class="gallery">
      <div class="photo-frame"><div class="photo photo-lamps" role="img" aria-label="Foto: Baustellen-Warnleuchten auf rot-weißen Leitbaken"></div></div>
      <div class="photo-frame"><div class="photo photo-road" role="img" aria-label="Foto: Firmentransporter an einer Landstraße bei Sonnenuntergang"></div></div>
      <div class="photo-frame"><div class="photo photo-sign" role="img" aria-label="Foto: Umleitungsschild vor einem weißen Firmentransporter"></div></div>
      <div class="photo-frame"><div class="photo photo-beacons" role="img" aria-label="Foto: Nahaufnahme gelber Warnleuchten an einer Baustellenabsperrung"></div></div>
    </section>

    <div class="footer-band" role="img" aria-label="Rot-weißes Warnstreifenband"></div>
  </main>
</body>
</html>
```